Vantrelo PowerPoint & Marketing Presentation

We need a powerpoint presentation for a marketing campaign. Attached is a powerpoint presentation that I did. It needs to be better. Much better. Our company - Vantrelo - is a start up that manages the coupon process for retailers and manufacturers. This powerpoint is a targeted presentation to a retailer.

We also need a hardcopy pamphlet to hand out at our meeting. The pamphlet should follow the powerpoint presentation, but not just be a copy of it. It should express whats in the powerpoint, but be a stand-alone document, which is easy to read.
Updates

Project Deadline Extended
Reason: Our internal project due date has been pushed back by a couple of weeks. While we can't extend the project by this amount, we can now afford an extra 5 days.

Target Market(s)

Corporate marketing and IT department

Industry/Entity Type

Marketing

Colors

Designer to choose colors to be used in the design.

Requirements
Must have
• Powerpoint presentation. Approximately 8-10 pages

```html
<!DOCTYPE html>
<html lang="en">
<head>
<meta charset="utf-8">
<title>Vantrelo Presentation Overview</title>
<link rel="stylesheet" href="https://fonts.googleapis.com/css2?family=Oswald:wght@400;500;700&family=Roboto:wght@400&display=swap">
<style>
  :root{
    --coral:#f2695a;
    --slate:#465066;
    --ink:#2b2f3a;
    --paper:#ffffff;
    --mist:#f3f3f4;
    --label:#3e4a66;
    --grey-text:#6b6f78;
  }
  *{box-sizing:border-box;margin:0;padding:0}
  html,body{width:1200px;height:849px;overflow:hidden;background:var(--paper)}
  body{position:relative;font-family:"Oswald",sans-serif;color:var(--ink)}
  .slide{position:absolute;width:371px;height:212px;border:2px solid var(--ink);background:var(--paper);overflow:hidden}
  .slide-label{position:absolute;width:371px;text-align:center;font-family:"Roboto",sans-serif;font-size:25px;letter-spacing:1px;color:var(--label)}
  .col-1{left:28px}.col-2{left:415px}.col-3{left:802px}
  .row-1{top:16px}.row-2{top:291px}.row-3{top:562px}
  .label-1{top:236px}.label-2{top:510px}.label-3{top:784px}
  .photo{position:absolute}
  .brand{font-family:"Oswald",sans-serif;font-weight:500;color:var(--coral);letter-spacing:.5px;white-space:nowrap}
  .accent-bar{position:absolute;background:var(--coral)}
  .top-band{position:absolute;left:96px;top:0;width:178px;height:9px;background:var(--coral)}
  .caption{position:absolute;text-align:center;font-size:7px;letter-spacing:1px;line-height:1.45;color:var(--grey-text)}
  .caption strong{display:block;font-weight:500;color:var(--coral);font-size:7.5px}
  .tiny-caps{font-size:7px;letter-spacing:1px;text-transform:uppercase}
  .store-aisle{background:linear-gradient(100deg,#c9b9a4 0%,#e9e3dc 40%,#b7a68f 70%,#8f8679 100%)}
  .snack-shelf{background:linear-gradient(160deg,#d6b56a,#c9574a 45%,#6a7fa6 80%,#e0d3b8)}
  .phone{position:absolute;background:#1e1f24;border-radius:7px}
  .phone-screen{position:absolute;left:4px;right:4px;top:9px;bottom:9px;background:#f5f2ee;border-radius:2px}
  .list{position:absolute;left:163px;top:6px;list-style:none}
  .list li{display:flex;align-items:center;height:34.5px;font-size:8.5px;color:var(--ink)}
  .list svg{width:16px;height:16px;margin-right:9px;flex:none}
</style>
</head>
<body>

<!-- Slide 1: title -->
<section class="slide col-1 row-1">
  <div class="photo store-aisle" role="img" aria-label="Shopper holding a smartphone beside a cart in a grocery aisle" style="left:0;top:0;width:143px;height:208px"></div>
  <div class="accent-bar" style="left:143px;top:17px;width:11px;height:191px"></div>
  <div class="brand" style="position:absolute;left:154px;width:213px;top:86px;text-align:center;font-size:22px">Vantrelo</div>
  <div class="tiny-caps" style="position:absolute;left:154px;width:213px;top:124px;text-align:center;font-weight:500;color:var(--ink)">Your complete digital coupon solution</div>
</section>
<div class="slide-label col-1 label-1">SLIDE 1</div>

<!-- Slide 2: flow -->
<section class="slide col-2 row-1">
  <div class="photo store-aisle" role="img" aria-label="Grocery aisle with a shopping cart in the foreground" style="left:0;top:0;width:143px;height:208px"></div>
  <div style="position:absolute;left:224px;top:21px">
    <div class="tiny-caps" style="font-weight:500;color:var(--ink)">Manufacturer coupons</div>
    <div style="font-size:7px;letter-spacing:1px;color:var(--grey-text)">To Customers</div>
  </div>
  <svg style="position:absolute;left:253px;top:51px" width="10" height="20" viewBox="0 0 10 20"><path d="M5 1 L9 7 H6.5 V19 H3.5 V7 H1 Z" fill="var(--slate)"/></svg>
  <div class="brand" style="position:absolute;left:143px;width:224px;top:86px;text-align:center;font-size:22px">Vantrelo</div>
  <svg style="position:absolute;left:253px;top:132px" width="10" height="20" viewBox="0 0 10 20"><path d="M5 19 L9 13 H6.5 V1 H3.5 V13 H1 Z" fill="var(--slate)"/></svg>
  <svg style="position:absolute;left:188px;top:162px" width="28" height="24" viewBox="0 0 28 24" fill="none" stroke="var(--slate)" stroke-width="1.4"><rect x="11" y="2" width="15" height="10" rx="1"/><path d="M11 5h15"/><path d="M2 22 L2 15 L8 14 L15 16 L19 15 L16 19 L8 21 Z"/></svg>
  <div style="position:absolute;left:221px;top:163px">
    <div class="tiny-caps" style="font-weight:500;color:var(--ink)">More customer spending</div>
    <div style="font-size:7px;letter-spacing:1px;color:var(--grey-text)">At Marlowe's</div>
  </div>
</section>
<div class="slide-label col-2 label-1">SLIDE 2</div>

<!-- Slide 3 -->
<section class="slide col-3 row-1">
  <div class="top-band"></div>
  <div class="brand" style="position:absolute;left:0;width:367px;top:24px;text-align:center;font-size:12px">Vantrelo</div>
  <div class="photo snack-shelf" role="img" aria-label="Snack shelf with a printed coupon hanging from it" style="left:0;top:47px;width:176px;height:115px"></div>
  <div class="photo snack-shelf" role="img" aria-label="Hand holding a phone showing a snack coupon in front of a shelf" style="left:193px;top:47px;width:174px;height:115px"></div>
  <div class="caption" style="left:0;width:176px;top:175px"><strong>COUPONS AVAILABLE</strong>RIGHT ON MARLOWE'S SHELVES</div>
  <div class="caption" style="left:193px;width:174px;top:175px"><strong>CUSTOMERS USE THEIR SMARTPHONES</strong>NO MORE CUTTING COUPONS</div>
</section>
<div class="slide-label col-3 label-1">SLIDE 3</div>

<!-- Slide 4 -->
<section class="slide col-1 row-2">
  <div class="top-band"></div>
  <div class="brand" style="position:absolute;left:0;width:367px;top:24px;text-align:center;font-size:12px">Vantrelo</div>
  <div class="photo snack-shelf" role="img" aria-label="Snack shelf with a printed coupon hanging from it" style="left:0;top:47px;width:176px;height:115px"></div>
  <div class="photo snack-shelf" role="img" aria-label="Hand holding a phone showing a snack coupon in front of a shelf" style="left:193px;top:47px;width:174px;height:115px"></div>
  <div class="caption" style="left:0;width:176px;top:175px"><strong>COUPONS AVAILABLE</strong>RIGHT ON MARLOWE'S SHELVES</div>
  <div class="caption" style="left:193px;width:174px;top:175px"><strong>CUSTOMERS USE THEIR SMARTPHONES</strong>NO MORE CUTTING COUPONS</div>
</section>
<div class="slide-label col-1 label-2">SLIDE 4</div>

<!-- Slide 5: steps -->
<section class="slide col-2 row-2">
  <div class="top-band"></div>
  <div class="brand" style="position:absolute;left:0;width:367px;top:24px;text-align:center;font-size:12px">Vantrelo</div>
  <div style="position:absolute;left:0;top:48px;width:121px;height:122px;background:var(--slate)">
    <div role="img" aria-label="Printed shelf coupon being scanned by a phone" style="position:absolute;left:20px;top:0;width:68px;height:96px;background:#f6f1ea"></div>
    <div class="phone" style="left:48px;top:76px;width:72px;height:36px"></div>
  </div>
  <div style="position:absolute;left:123px;top:48px;width:121px;height:122px;background:var(--slate)">
    <div class="phone" style="left:36px;top:4px;width:50px;height:110px"><div class="phone-screen" role="img" aria-label="Coupon added screen in the app"></div></div>
  </div>
  <div style="position:absolute;left:246px;top:48px;width:121px;height:122px;background:var(--slate)">
    <div class="phone" style="left:36px;top:4px;width:50px;height:110px"><div class="phone-screen" role="img" aria-label="Coupon queue screen with a check-out button"></div></div>
  </div>
  <div class="caption" style="left:0;width:121px;top:173px"><strong>STEP 1</strong>SCAN COUPON BARCODE</div>
  <div class="caption" style="left:123px;width:121px;top:173px"><strong>STEP 2</strong>COUPON AUTOMATICALLY ADDED TO CUSTOMER'S VANTRELO QUEUE</div>
  <div class="caption" style="left:246px;width:121px;top:173px"><strong>STEP 3</strong>CHECK OUT</div>
</section>
<div class="slide-label col-2 label-2">SLIDE 5</div>

<!-- Slide 6 -->
<section class="slide col-3 row-2">
  <div style="position:absolute;left:0;top:0;width:154px;height:208px;background:var(--mist)"></div>
  <div style="position:absolute;left:154px;top:0;width:213px;height:208px;background:var(--slate)" role="img" aria-label="Phone showing a scan-now coupon next to a checkout barcode scanner"></div>
  <div class="accent-bar" style="left:143px;top:15px;width:11px;height:179px"></div>
  <div style="position:absolute;left:14px;top:95px;width:128px;font-size:7.5px;letter-spacing:.8px;line-height:1.5">
    <div style="font-weight:500;color:var(--ink)">SINGLE SCAN LOADS COUPONS</div>
    <div style="color:var(--coral)">DIRECTLY TO MARLOWE'S POS</div>
  </div>
</section>
<div class="slide-label col-3 label-2">SLIDE 6</div>

<!-- Slide 7: benefits -->
<section class="slide col-1 row-3">
  <div style="position:absolute;left:0;top:0;width:145px;height:208px;background:var(--slate)"></div>
  <div style="position:absolute;left:145px;top:0;width:222px;height:208px;background:var(--mist)"></div>
  <div class="accent-bar" style="left:145px;top:15px;width:11px;height:183px"></div>
  <div class="brand" style="position:absolute;left:0;width:145px;top:78px;text-align:center;font-size:22px">Vantrelo</div>
  <div style="position:absolute;left:0;width:145px;top:124px;text-align:center;font-size:7.5px;letter-spacing:1px;line-height:1.6;color:var(--coral)">MANAGES COUPON REDEMPTION<br>PROCESS FOR MARLOWE'S</div>
  <ul class="list">
    <li><svg viewBox="0 0 16 16" fill="var(--slate)"><ellipse cx="5" cy="5" rx="2.5" ry="4"/><ellipse cx="11" cy="9" rx="2.5" ry="4"/></svg>Increased foot-traffic</li>
    <li><svg viewBox="0 0 16 16" fill="none" stroke="var(--slate)" stroke-width="1.4"><path d="M1 2h3l2 8h8l1.5-6H5"/><circle cx="7" cy="13.5" r="1.2" fill="var(--slate)"/><circle cx="13" cy="13.5" r="1.2" fill="var(--slate)"/></svg>Higher in-cart purchases</li>
    <li><svg viewBox="0 0 16 16"><circle cx="8" cy="8" r="7.5" fill="var(--slate)"/><path d="M8 3.5V8h3.5" stroke="#fff" stroke-width="1.4" fill="none"/></svg>Real-Time Monitoring of Coupon Usage</li>
    <li><svg viewBox="0 0 16 16" fill="none" stroke="var(--slate)" stroke-width="1.2"><rect x="3" y="1" width="10" height="14" rx="1"/><path d="M5.5 5h5M5.5 8h5M5.5 11h3"/></svg>Reports of Coupon Activity</li>
    <li><svg viewBox="0 0 16 16" fill="none" stroke="var(--slate)" stroke-width="1.2"><rect x="1" y="3" width="14" height="10" rx="1"/><path d="M4 8h8"/></svg>Smooth Coupon Redemption Managed by Vantrelo</li>
    <li><svg viewBox="0 0 16 16" fill="none" stroke="var(--slate)" stroke-width="1.2"><rect x="1" y="1" width="8" height="8" rx="1"/><path d="M5 3v4M8 9v5l2-1 2 2 2-3-2-2h-2"/></svg>Faster Payment for Coupons after Redemption</li>
  </ul>
</section>
<div class="slide-label col-1 label-3">SLIDE 7</div>

<!-- Slide 8: closing -->
<section class="slide col-2 row-3">
  <div class="photo" role="img" aria-label="Supermarket checkout lanes in a muted blue-grey tone" style="left:0;top:0;width:367px;height:208px;background:linear-gradient(180deg,#8b93a3,#6f7889 55%,#5e6676)"></div>
  <div class="top-band"></div>
  <div style="position:absolute;left:96px;bottom:0;width:178px;height:9px;background:var(--coral)"></div>
  <div style="position:absolute;left:0;width:367px;top:52px;text-align:center;font-weight:700;font-size:44px;letter-spacing:.5px;color:var(--coral)">THANK YOU!</div>
  <div class="brand" style="position:absolute;left:0;width:367px;top:148px;text-align:center;font-size:22px">Vantrelo</div>
</section>
<div class="slide-label col-2 label-3">SLIDE 8</div>

</body>
</html>
```